Post it Note design

POST-IT NOTE DESIGN (CONTENT)
Size recommended: 4x6 for handwriting space.
Header (Bold):
Lighting Issue Detected on Your Property
Sub-header:
During our routine night inspection, we noted the following item(s):
Checkbox List:
⬜ Building Lights Out
⬜ Pole Lights Out
⬜ Sign Not Illuminated
⬜ Other ________________________
Action Line:
We can provide a quote or dispatch service right away.
Area for notes
Contact Block (Bold & Centered):
Brovane Fixture Inc.
Service@BrovaneFixture.com
www.BrovaneFixture.com
877-514-0862
Industry/Entity Type
Electrical lighting
Colors
Designer to choose colors to be used in the design.
Look and feel
Each slider illustrates characteristics of the customer's brand and the style your logo design should communicate.

```html
<!DOCTYPE html>
<html lang="en">
<head>
<meta charset="utf-8">
<title>Brovane Fixture Inc. – Inspection Note</title>
<link href="https://fonts.googleapis.com/css2?family=Poppins:wght@500;600;700&display=swap" rel="stylesheet">
<style>
  :root {
    --red: #d0142c;
    --navy: #0b1a8e;
    --paper: #ffffff;
    --backdrop: #c1c1c1;
    --photo-sky: #6f97cf;
    --photo-sky-light: #a9c3e6;
    --truck: #e4e6ea;
  }
  * { box-sizing: border-box; margin: 0; padding: 0; }
  html, body {
    width: 1200px; height: 952px; overflow: hidden;
    background: var(--backdrop);
    font-family: "Poppins", sans-serif;
  }
  .note {
    position: absolute; top: 170px;
    width: 408px; height: 612px;
    background: var(--paper);
    overflow: hidden;
  }
  .note--red { left: 144px; }
  .note--navy { left: 635px; }

  .vehicle {
    position: absolute; top: 30px; height: 56px;
    background: linear-gradient(180deg, #f4f5f7, var(--truck) 70%, #9a9ea6);
    border-radius: 6px;
  }
  .vehicle--left { left: 23px; width: 90px; }
  .vehicle--right { left: 294px; width: 92px; }

  .brand {
    position: absolute; top: 38px; left: 113px; width: 181px;
    text-align: center;
    color: var(--red); font-weight: 700;
    font-size: 20px; line-height: 22px;
  }
  .brand__mark {
    display: block; width: 12px; height: 12px;
    background: var(--navy); margin: 0 auto 4px;
  }

  .headline {
    position: absolute; top: 110px; left: 0; width: 100%;
    text-align: center; color: var(--navy);
    font-weight: 700; font-size: 20px; line-height: 27px;
  }

  .band {
    position: absolute; left: 0; width: 100%;
    background: var(--red); color: #fff;
    text-align: center; font-weight: 600;
    border-top: 2px solid var(--paper);
    border-bottom: 2px solid var(--paper);
    box-shadow: 0 -2px 0 var(--navy), 0 2px 0 var(--navy);
  }
  .band--intro { top: 176px; height: 24px; font-size: 10px; line-height: 20px; letter-spacing: -0.2px; }
  .band--action { top: 343px; height: 24px; font-size: 11.5px; line-height: 20px; letter-spacing: 0.3px; }

  .checklist {
    position: absolute; top: 222px; left: 33px;
    list-style: none;
  }
  .checklist li {
    display: flex; align-items: center;
    height: 29px; color: var(--navy);
    font-weight: 600; font-size: 12px;
  }
  .checklist .box {
    width: 15px; height: 15px; border: 1.5px solid var(--red);
    margin-right: 6px; flex: none;
  }

  .photo {
    position: absolute; top: 202px; left: 214px;
    width: 194px; height: 139px;
    background: linear-gradient(160deg, var(--photo-sky-light), var(--photo-sky) 60%, #8c9099);
  }

  .notes-area { position: absolute; top: 370px; left: 0; width: 100%; height: 170px; }

  .contact {
    position: absolute; top: 543px; left: 0; width: 100%; height: 69px;
    color: #fff; text-align: center;
    font-weight: 600; font-size: 12px; line-height: 17.5px;
    padding-top: 5px; letter-spacing: 0.4px;
    border-top: 2px solid var(--paper);
    box-shadow: 0 -2px 0 var(--navy);
  }
  .note--red .contact { background: var(--red); }
  .note--navy .contact { background: var(--navy); box-shadow: 0 -2px 0 var(--red); }
  .contact .phone { letter-spacing: 2.5px; }
</style>
</head>
<body>

<article class="note note--red">
  <div class="vehicle vehicle--left" role="img" aria-label="Photo of a white bucket truck"></div>
  <div class="brand"><span class="brand__mark"></span>Brovane Fixture Inc.</div>
  <div class="vehicle vehicle--right" role="img" aria-label="Photo of a white service van"></div>
  <h1 class="headline">Lighting Issue Detected on<br>Your Property</h1>
  <p class="band band--intro">During our routine night inspection, we noted the following item(s):</p>
  <ul class="checklist">
    <li><span class="box"></span>Building Lights Out</li>
    <li><span class="box"></span>Pole Lights Out</li>
    <li><span class="box"></span>Sign Not Illuminated</li>
    <li><span class="box"></span>Other ___________</li>
  </ul>
  <div class="photo" role="img" aria-label="Photo of a technician servicing pole lamps against a blue sky"></div>
  <p class="band band--action">We can provide a quote or dispatch service right away.</p>
  <div class="notes-area"></div>
  <footer class="contact">
    Service@BrovaneFixture.com<br>
    www.BrovaneFixture.com<br>
    <span class="phone">877-514-0862</span>
  </footer>
</article>

<article class="note note--navy">
  <div class="vehicle vehicle--left" role="img" aria-label="Photo of a white bucket truck"></div>
  <div class="brand"><span class="brand__mark"></span>Brovane Fixture Inc.</div>
  <div class="vehicle vehicle--right" role="img" aria-label="Photo of a white service van"></div>
  <h1 class="headline">Lighting Issue Detected on<br>Your Property</h1>
  <p class="band band--intro">During our routine night inspection, we noted the following item(s):</p>
  <ul class="checklist">
    <li><span class="box"></span>Building Lights Out</li>
    <li><span class="box"></span>Pole Lights Out</li>
    <li><span class="box"></span>Sign Not Illuminated</li>
    <li><span class="box"></span>Other ___________</li>
  </ul>
  <div class="photo" role="img" aria-label="Photo of a technician servicing pole lamps against a blue sky"></div>
  <p class="band band--action">We can provide a quote or dispatch service right away.</p>
  <div class="notes-area"></div>
  <footer class="contact">
    Service@BrovaneFixture.com<br>
    www.BrovaneFixture.com<br>
    <span class="phone">877-514-0862</span>
  </footer>
</article>

</body>
</html>
```